Sunvale Energy UK Flyer Design, for local domestic and commercial properties.

We are a renewable energy company called "SUNVALE ENERGY UK" we specialize in
Electrical and renewable energy project consultancy.
Solar panel installations
battery storage.
Electrical design and installation from Stage 3

Details can be found on our website: www.sunvaleenergyuk.co.uk
Am looking to have a flyer designed so we can have printed and delivered to all local areas.
We carry out free project surveys and offer full project transparency through out the clients journey.
attached is our logo of which i hope may help.

Target Market(s)

Domestic and commercial properties looking to dramatically reduce energy bills

Industry/Entity Type

Domestic, commercial, industrial, mixed used development and much more.

Font styles to use
Serif
Sans Serif
Decorative

Colors
FFC000
F8CF3A
FAE287
FDF2CF
FEFAEE
F0912C
F2A743
F7CA91
FBE8D2
FDF5EE
EE7325
F08F49
F5BC92
FAE3D3
FDF4ED

Requirements
Must have
• Highlight we offer free quotations and offer a fully transparent project processes from design, installation Plus leading health and safety process no matter what size project.
Nice to have
• Pictures of solar panel systems, i have attached a few pictures which you may wish to edit or take snippets etc.

```html
<!DOCTYPE html>
<html lang="en">
<head>
<meta charset="utf-8">
<title>Sunvale Energy UK Flyer</title>
<link href="https://fonts.googleapis.com/css2?family=Montserrat:wght@300;400;600;700&family=Oswald:wght@500;600;700&display=swap" rel="stylesheet">
<style>
  :root {
    --gold: #FFC000;
    --butter: #FAE287;
    --cream: #FDF2CF;
    --amber: #F0912C;
    --apricot: #F2A743;
    --peach: #F7CA91;
    --orange: #EE7325;
    --burnt: #D9621F;
    --rust: #C9561A;
    --ink: #1e1e1e;
    --text-grey: #333333;
    --white: #ffffff;
    --stage: #e9e6e1;
  }
  * { box-sizing: border-box; margin: 0; padding: 0; }
  html, body { width: 1200px; height: 1200px; overflow: hidden; background: var(--stage); }
  body { font-family: "Montserrat", Arial, sans-serif; }

  .flyer {
    position: absolute; left: 200px; top: 35px;
    width: 800px; height: 1130px; overflow: hidden;
    background: var(--white);
    box-shadow: 0 10px 30px rgba(0,0,0,.25);
  }
  .artwork { position: absolute; left: 0; top: 0; }

  .logo {
    position: absolute; left: 60px; top: 180px;
    display: flex; align-items: center; gap: 16px;
  }
  .logo-dot { width: 48px; height: 48px; border-radius: 50%; background: var(--amber); }
  .logo-name {
    font-weight: 600; font-size: 28px; letter-spacing: 4px;
    color: var(--ink); line-height: 1.15;
  }

  .badge-text {
    position: absolute; left: 520px; top: 325px; width: 200px;
    transform: rotate(-18deg);
    font-family: "Oswald", Arial, sans-serif; font-weight: 600;
    font-size: 19px; line-height: 1.05; color: var(--white);
    text-transform: uppercase; text-align: center;
    text-shadow: 0 1px 2px rgba(120,50,0,.6);
  }

  .intro {
    position: absolute; left: 55px; top: 690px; width: 330px;
    font-weight: 300; font-size: 16px; line-height: 1.45; color: var(--white);
    letter-spacing: .5px;
  }
  .services { position: absolute; left: 55px; top: 800px; width: 345px; list-style: none; }
  .service { display: flex; align-items: center; gap: 18px; height: 92px; }
  .service-icon { flex: 0 0 62px; width: 62px; height: 62px; }
  .service-name {
    font-weight: 700; font-size: 14.5px; line-height: 1.2; color: var(--white);
    text-transform: uppercase; letter-spacing: .5px;
  }

  .divider {
    position: absolute; left: 405px; top: 625px; height: 410px;
    border-left: 3px dotted rgba(255,255,255,.85);
  }
  .promise {
    position: absolute; left: 430px; top: 622px; width: 345px;
    font-family: "Oswald", Arial, sans-serif; font-weight: 600;
    font-size: 25px; line-height: 1.12; color: var(--butter);
    text-transform: uppercase;
  }

  .contact { position: absolute; left: 522px; top: 905px; width: 270px; font-style: normal; }
  .contact-line {
    display: flex; align-items: center; gap: 10px;
    font-family: "Oswald", Arial, sans-serif; font-weight: 500;
    font-size: 19px; color: var(--text-grey); margin-bottom: 8px; white-space: nowrap;
  }
  .contact-line .accent { color: var(--rust); }
  .contact-phone { font-size: 34px; font-weight: 700; color: var(--rust); margin-top: 4px; }
  .contact-line svg { flex: 0 0 auto; }
</style>
</head>
<body>
  <main class="flyer">
    <svg class="artwork" width="800" height="1130" viewBox="0 0 800 1130">
      <defs>
        <linearGradient id="paper" x1="0" y1="0" x2="0.4" y2="1">
          <stop offset="0" stop-color="#ffffff"/>
          <stop offset="1" stop-color="#dbe7f5"/>
        </linearGradient>
        <linearGradient id="roofTones" x1="0" y1="0" x2="0" y2="1">
          <stop offset="0" stop-color="#a9c9ec"/>
          <stop offset=".22" stop-color="#8fb0d6"/>
          <stop offset=".34" stop-color="#3c4454"/>
          <stop offset=".7" stop-color="#2b313c"/>
          <stop offset=".86" stop-color="#9c5a42"/>
          <stop offset="1" stop-color="#c9b59a"/>
        </linearGradient>
        <linearGradient id="fadeLeft" x1="0" y1="0" x2="1" y2="0">
          <stop offset="0" stop-color="#000"/>
          <stop offset=".35" stop-color="#fff"/>
        </linearGradient>
        <mask id="roofMask"><rect x="300" y="0" width="500" height="600" fill="url(#fadeLeft)"/></mask>
        <linearGradient id="coupleTones" x1="0" y1="0" x2="1" y2="1">
          <stop offset="0" stop-color="#cfd2d6"/>
          <stop offset="1" stop-color="#a9adb2"/>
        </linearGradient>
        <linearGradient id="arrayTones" x1="0" y1="0" x2="0.6" y2="1">
          <stop offset="0" stop-color="#D9621F"/>
          <stop offset=".4" stop-color="#a8450f"/>
          <stop offset="1" stop-color="#c4561a"/>
        </linearGradient>
        <linearGradient id="fadeTop" x1="0" y1="0" x2="0" y2="1">
          <stop offset="0" stop-color="#000"/>
          <stop offset=".3" stop-color="#fff"/>
        </linearGradient>
        <mask id="arrayMask"><rect x="415" y="760" width="385" height="370" fill="url(#fadeTop)"/></mask>
        <linearGradient id="houseTones" x1="0" y1="0" x2="0" y2="1">
          <stop offset="0" stop-color="#9cc3ea"/>
          <stop offset=".35" stop-color="#9cc3ea"/>
          <stop offset=".5" stop-color="#3b3f48"/>
          <stop offset=".75" stop-color="#a07a58"/>
          <stop offset="1" stop-color="#c4a882"/>
        </linearGradient>
        <linearGradient id="burst" x1="0" y1="0" x2="1" y2="1">
          <stop offset="0" stop-color="#FFC000"/>
          <stop offset=".5" stop-color="#F2A743"/>
          <stop offset="1" stop-color="#EE7325"/>
        </linearGradient>
        <pattern id="dots" width="14" height="14" patternUnits="userSpaceOnUse">
          <circle cx="7" cy="7" r="1.3" fill="#ffffff" opacity=".12"/>
        </pattern>
      </defs>

      <rect width="800" height="1130" fill="url(#paper)"/>

      <rect x="300" y="0" width="500" height="600" fill="url(#roofTones)" mask="url(#roofMask)"
            role="img" aria-label="Photo of a tiled house roof fitted with black solar panels and scaffolding against a blue sky"/>

      <rect x="150" y="340" width="310" height="300" rx="150" fill="url(#coupleTones)"
            role="img" aria-label="Photo of a smiling couple pointing up towards the solar panels"/>

      <path d="M0 590 Q 300 665 560 520 L 800 420 L 800 1130 L 0 1130 Z" fill="#F7CA91"/>
      <path d="M0 605 Q 300 680 570 530 L 800 432 L 800 1130 L 0 1130 Z" fill="#ffffff"/>
      <path d="M0 615 Q 300 692 575 540 L 800 440 L 800 1130 L 0 1130 Z" fill="#D9621F"/>
      <path d="M0 615 Q 300 692 575 540 L 800 440 L 800 1130 L 0 1130 Z" fill="url(#dots)"/>

      <rect x="415" y="760" width="385" height="370" fill="url(#arrayTones)" mask="url(#arrayMask)"
            role="img" aria-label="Orange-tinted photo of a large ground-mounted solar panel array"/>

      <circle cx="800" cy="1130" r="338" fill="#ffffff" stroke="#F5A06A" stroke-width="16"/>

      <polygon transform="translate(615 380)" fill="url(#burst)" stroke="#F7CA91" stroke-width="3"
        points="0,-125 20,-100 45,-115 52,-86 82,-92 78,-62 108,-55 92,-30 118,-12 95,8 115,32 86,42 95,72 65,72 62,103 35,92 20,120 0,100 -20,120 -35,92 -62,103 -65,72 -95,72 -86,42 -115,32 -95,8 -118,-12 -92,-30 -108,-55 -78,-62 -82,-92 -52,-86 -45,-115 -20,-100"/>

      <circle cx="475" cy="480" r="76" fill="url(#houseTones)" stroke="#ffffff" stroke-width="5"
              role="img" aria-label="Photo of a stone house with new solar panels on its roof"/>
    </svg>

    <div class="logo">
      <span class="logo-dot"></span>
      <span class="logo-name">SUNVALE<br>ENERGY UK</span>
    </div>

    <p class="badge-text">Free project surveys and offer full project transparency</p>

    <p class="intro">We carry out free project surveys and offer full project transparency through out the clients journey.</p>

    <ul class="services">
      <li class="service">
        <svg class="service-icon" viewBox="0 0 62 62" fill="none" stroke="#F7CA91" stroke-width="2.2" stroke-linecap="round" stroke-linejoin="round" aria-hidden="true">
          <path d="M22 40c0-6-8-9-8-18a13 13 0 0 1 26 0c0 9-8 12-8 18z"/>
          <path d="M22 45h10M23 50h8"/>
          <path d="M27 36V26M27 28c-4 0-6-3-6-6 3 0 6 2 6 6zM27 28c4 0 6-3 6-6-3 0-6 2-6 6z"/>
          <path d="M48 10v32M44 42h8v5h-8zM46 47v6M50 47v6"/>
        </svg>
        <span class="service-name">Electrical and renewable project consultancy.</span>
      </li>
      <li class="service">
        <svg class="service-icon" viewBox="0 0 62 62" fill="none" stroke="#F7CA91" stroke-width="2.2" stroke-linecap="round" stroke-linejoin="round" aria-hidden="true">
          <circle cx="44" cy="14" r="5"/>
          <path d="M44 4v3M52 14h3M50 8l2-2M36 8l-2-2"/>
          <path d="M12 22h32l6 22H6z"/>
          <path d="M9 33h38M22 22l-3 22M33 22l2 22"/>
          <path d="M28 44v8M20 54h16"/>
        </svg>
        <span class="service-name">Solar panel installations</span>
      </li>
      <li class="service">
        <svg class="service-icon" viewBox="0 0 62 62" fill="none" stroke="#F7CA91" stroke-width="2.2" stroke-linecap="round" stroke-linejoin="round" aria-hidden="true">
          <rect x="8" y="18" width="46" height="34" rx="3"/>
          <path d="M14 18v-5h8v5M40 18v-5h8v5"/>
          <path d="M33 24l-8 12h7l-3 10 9-13h-7z"/>
          <path d="M13 30h6M16 27v6M44 30h6"/>
        </svg>
        <span class="service-name">Battery storage.</span>
      </li>
    </ul>

    <div class="divider"></div>
    <p class="promise">Free quotations and installation and health and safety process no matter what size project.</p>

    <address class="contact">
      <div class="contact-line">
        <svg width="18" height="22" viewBox="0 0 18 22" aria-hidden="true"><path d="M9 1a7 7 0 0 0-7 7c0 5 7 12 7 12s7-7 7-12a7 7 0 0 0-7-7z" fill="none" stroke="#C9561A" stroke-width="2"/><circle cx="9" cy="8" r="2.5" fill="#C9561A"/></svg>
        Your Address Here
      </div>
      <div class="contact-line">
        <svg width="20" height="20" viewBox="0 0 20 20" aria-hidden="true"><circle cx="10" cy="10" r="8" fill="none" stroke="#C9561A" stroke-width="2"/><path d="M2 10h16M10 2c3 3 3 13 0 16M10 2c-3 3-3 13 0 16" fill="none" stroke="#C9561A" stroke-width="1.5"/></svg>
        <span>www.<span class="accent">sunvaleenergyuk</span>.co.uk</span>
      </div>
      <div class="contact-line contact-phone">
        <svg width="26" height="26" viewBox="0 0 24 24" aria-hidden="true"><path d="M6.6 10.8a15 15 0 0 0 6.6 6.6l2.2-2.2a1 1 0 0 1 1-.25 11.4 11.4 0 0 0 3.6.57 1 1 0 0 1 1 1V20a1 1 0 0 1-1 1A17 17 0 0 1 3 4a1 1 0 0 1 1-1h3.5a1 1 0 0 1 1 1c0 1.25.2 2.45.57 3.57a1 1 0 0 1-.25 1z" fill="#C9561A"/></svg>
        600.555.0142
      </div>
    </address>
  </main>
</body>
</html>
```